Global lighting company needs compelling e-tail graphic

Our company is a global lighting company that sells light bulbs, lighting fixtures and ceiling fans. For this project, we have a concept developed for a graphic that explains color temperature for LED light bulbs. We would like to develop this concept into something more exciting and polished for consumer-friendly use on our e-tail product pages.Color temperature, in simple terms, is the ambience and atmosphere created by the color of a light bulb. More detailed information about color temperature can be found here: http://www.brambleforgelamps.com/color-temperature.aspx

Target Market(s)

Online consumers, homeowners

Industry/Entity Type

Lighting Fixture

Font styles to use
Sans Serif

Colors

Designer to choose colors to be used in the design.

Requirements
Must have
• Images depicting color temperature, preferably residential room scenes

```html
<!DOCTYPE html>
<html lang="en">
<head>
<meta charset="utf-8">
<title>Color temperature affects the mood and ambience of a room</title>
<link rel="stylesheet" href="https://fonts.googleapis.com/css2?family=Nunito+Sans:wght@400;600;800&display=swap">
<style>
  :root {
    --ink: #3a3a3c;
    --label: #4a4a4c;
    --rule: #b9b9bb;
    --scale-text: #5d5d60;
    --scale-muted: #8e8e90;
    --paper: #ffffff;
    --warm-deep: #f0806a;
    --warm-mid: #f7c37a;
    --warm-light: #fbeea8;
    --neutral: #ffffff;
    --cool-light: #cfe6f5;
    --cool-mid: #7fc0ea;
    --daylight: #1e8fd0;
  }
  * { box-sizing: border-box; margin: 0; padding: 0; }
  html, body { width: 1200px; height: 761px; overflow: hidden; background: var(--paper); }
  body { font-family: "Nunito Sans", sans-serif; color: var(--ink); }

  .graphic { position: relative; width: 1200px; height: 761px; }

  .headline {
    position: absolute; left: 67px; top: 30px;
    font-size: 44px; font-weight: 800; line-height: 1.5; letter-spacing: -0.2px;
  }

  .moods { position: absolute; left: 48px; top: 185px; width: 1108px; height: 86px; display: flex; }
  .mood {
    flex: 1; display: flex; align-items: center; justify-content: center;
    text-align: center; font-size: 18px; font-weight: 600; letter-spacing: 6px;
    line-height: 1.55; color: var(--label); padding-bottom: 14px;
  }
  .mood + .mood { border-left: 1px solid var(--rule); }

  .scenes { position: absolute; left: 48px; top: 271px; width: 1108px; height: 359px; display: flex; }
  .scene { flex: 1; height: 100%; }
  .scene--cozy { background: linear-gradient(160deg, #6b3a17 0%, #b86a2c 40%, #8a4a22 75%, #4a2410 100%); }
  .scene--inviting { background: linear-gradient(175deg, #f3f1ee 0%, #e8e4de 55%, #a59c92 85%, #6e655c 100%); }
  .scene--vibrant { background: linear-gradient(180deg, #f4f6fa 0%, #c9d3e2 40%, #e7ecf3 60%, #ffffff 80%, #f0f2f6 100%); }
  .scene--crisp { background: linear-gradient(170deg, #dbe9f7 0%, #b9d3ef 45%, #e4eef9 80%, #f4f8fd 100%); }

  .shades { position: absolute; left: 48px; top: 271px; }

  .scale {
    position: absolute; left: 48px; top: 630px; width: 1108px; height: 94px;
    background: linear-gradient(90deg, var(--warm-deep) 0%, var(--warm-mid) 14%, var(--warm-light) 26%, var(--neutral) 38%, var(--neutral) 44%, var(--cool-light) 56%, var(--cool-mid) 76%, var(--daylight) 100%);
  }
  .scale-value, .scale-name { position: absolute; transform: translateX(-50%); white-space: nowrap; }
  .scale-value { top: 14px; font-size: 16px; font-weight: 400; color: var(--paper); opacity: 0.85; }
  .scale-value--dim { color: var(--scale-muted); opacity: 1; }
  .scale-name { top: 46px; font-size: 15px; font-weight: 600; letter-spacing: 5.5px; color: var(--scale-text); }

  .ticks { position: absolute; left: 0; top: 0; }
</style>
</head>
<body>
<main class="graphic">
  <h1 class="headline">Color temperature affects the mood<br>and ambience of a room</h1>

  <div class="moods">
    <p class="mood">COZY<br>CALM</p>
    <p class="mood">INVITING<br>BRIGHT</p>
    <p class="mood">VIBRANT<br>COOL</p>
    <p class="mood">CRISP<br>INVIGORATING</p>
  </div>

  <div class="scenes">
    <div class="scene scene--cozy" role="img" aria-label="Living room with a table lamp and fireplace in warm amber light"></div>
    <div class="scene scene--inviting" role="img" aria-label="Bright living room with chandelier, fireplace and sofa"></div>
    <div class="scene scene--vibrant" role="img" aria-label="White kitchen with under-cabinet lighting and bar stools"></div>
    <div class="scene scene--crisp" role="img" aria-label="Daylit breakfast nook with window and white table"></div>
  </div>

  <svg class="shades" width="1108" height="359" viewBox="0 0 1108 359" aria-hidden="true">
    <g fill="none" stroke="#ffffff" stroke-width="1.5" opacity="0.9">
      <polyline points="58,0 58,78 132,134 210,78 210,0"/>
      <polyline points="290,0 290,60 406,134 490,60 490,0"/>
      <polyline points="570,0 570,82 695,134 824,82 824,0"/>
      <polyline points="896,0 896,92 1014,134 1106,92 1106,0"/>
    </g>
  </svg>

  <div class="scale">
    <span class="scale-value" style="left:145px">2,700K</span>
    <span class="scale-value scale-value--dim" style="left:418px">3,000K</span>
    <span class="scale-value scale-value--dim" style="left:688px">4,000K</span>
    <span class="scale-value" style="left:964px">5,000K</span>
    <span class="scale-name" style="left:326px">WARM WHITE</span>
    <span class="scale-name" style="left:690px">COOL WHITE</span>
    <span class="scale-name" style="left:962px">DAYLIGHT</span>
  </div>

  <svg class="ticks" width="1200" height="761" viewBox="0 0 1200 761" aria-hidden="true">
    <g fill="var(--rule)">
      <circle cx="322" cy="191" r="2.5"/>
      <circle cx="600" cy="191" r="2.5"/>
      <circle cx="880" cy="191" r="2.5"/>
      <polygon points="318,724 326,724 322,717"/>
      <polygon points="596,724 604,724 600,717"/>
      <polygon points="876,724 884,724 880,717"/>
      <polygon points="318,630 326,630 322,637"/>
      <polygon points="596,630 604,630 600,637"/>
      <polygon points="876,630 884,630 880,637"/>
    </g>
  </svg>
</main>
</body>
</html>
```